New Writer Needs Website to Showcase Her Work

I'm a new writer of literary fiction. Several of my short stories have been published in literary journals, with more to come. I'm working on my first novel, and one of my stories will be featured in a "best of" anthology that will hit bookstores soon. I am not online at all at the moment (allergic to social media), but I would like readers, editors and agents to be able to find me if they like my work. Also, I'm told that editors and agents are more likely to take a chance with a writer who promotes her work online, hence my project. I've uploaded a few of my (very short) stories to give you the flavor of who I am as a writer. I write for adults, and my fiction has a dark edge to it. Not Harold Vance dark, not BRV dark, more like unhappy people trying to make their way in a world that demands happiness. If I were so lucky as to write a movie, I'd write a quirky, brooding, independent film, not a summer blockbuster. Think Lanterns Over Pellworth, not Avalanche. Thank you for your help!

Target Market(s)

Literary editors, agents, publishers and readers.

Industry/Entity Type

Work

Logo Text

Tessa Ward Finch

Number of Pages Required

1 page

Font styles to use
Serif
Sans Serif

Colors

Designer to choose colors to be used in the design.

Requirements
Must have
• Weight. I write serious stories, and I want that to come through. I will want to add links to my stories that are published online, notices for upcoming speaking engagements, publications, news, etc. I'll want a Bio section or page. I really don't know how many pages would be optimal, so I'm open to suggestions.
Nice to have
• Darker colors, but not anything obvious like black. Please resist the temptation to incorporate roses into your design.
Should not have
• Anything cute or fussy. I like clean lines, simple designs that draw you in with their beauty.

```html
<!DOCTYPE html>
<html lang="en">
<head>
<meta charset="utf-8">
<title>Tessa Finch — Author</title>
<link href="https://fonts.googleapis.com/css2?family=Lobster&family=Open+Sans:wght@400;600;700&display=swap" rel="stylesheet">
<style>
:root{
  --night:#1b1433;
  --purple:#3e2372;
  --purple-deep:#2f1a5a;
  --white:#ffffff;
  --muted:#d9d2ea;
  --line:#b9a8dc;
  --wood:#6b4128;
}
*{margin:0;padding:0;box-sizing:border-box}
html,body{width:1200px;height:2961px;overflow:hidden}
body{font-family:"Open Sans",Arial,sans-serif;color:var(--white);background:var(--purple);position:relative}
.script{font-family:"Lobster",Georgia,cursive;font-weight:400}
section,header,footer{position:absolute;left:0;width:1200px}
.btn{position:absolute;border:2px solid var(--white);border-radius:24px;color:var(--white);font-size:14px;font-weight:600;display:flex;align-items:center;justify-content:center;text-decoration:none;letter-spacing:.3px}

/* header */
.site-header{top:0;height:110px;background:var(--night)}
.brand{position:absolute;left:99px;top:28px;font-size:46px}
.main-nav{position:absolute;right:98px;top:46px;display:flex;gap:48px;font-size:16px;font-weight:600}
.main-nav a{color:var(--white);text-decoration:none}

/* hero */
.hero{top:110px;height:590px}
.hero-photo{position:absolute;inset:0;background:linear-gradient(100deg,#3d5a3a 0%,#6f8a5c 30%,#9aa97a 50%,#6c6a4b 70%,#4a3b2c 100%)}
.hero-title{position:absolute;left:99px;top:185px;font-size:64px}
.hero-tagline{position:absolute;left:99px;top:285px;font-size:20px}
.hero .btn{left:99px;top:340px;width:128px;height:44px}
.curve{position:absolute;left:0;width:1200px}
.hero .curve{bottom:0;height:40px}
.dots{position:absolute;left:568px;top:573px;display:flex;gap:6px}
.dots span{width:14px;height:14px;border-radius:50%;border:2px solid var(--white)}
.dots span.on{background:var(--white)}

/* about */
.about{top:700px;height:417px;background:var(--purple)}
.about-portrait{position:absolute;left:99px;top:86px;width:316px;height:233px;border-radius:50%;border:3px solid var(--white);background:radial-gradient(ellipse at 50% 45%,#c99a7a 0%,#8b6a55 40%,#7a8a6c 100%)}
.about-title{position:absolute;left:480px;top:72px;font-size:40px}
.about-greet{position:absolute;left:480px;top:146px;font-size:17px;font-weight:700}
.about-text{position:absolute;left:480px;top:186px;width:640px;font-size:11.6px;line-height:25px;color:var(--muted)}
.about .btn{left:480px;top:280px;width:140px;height:40px}

/* speaking */
.speaking{top:1117px;height:367px}
.speaking-photo{position:absolute;inset:0;background:linear-gradient(90deg,var(--wood) 0%,#8a5a3a 8%,#c8bfb2 30%,#e6e0d6 60%,#b7aa98 92%,var(--wood) 100%)}
.speaking-panel{position:absolute;left:99px;top:0;width:286px;height:367px;background:rgba(62,35,114,.85)}
.speaking-title{position:absolute;left:126px;top:84px;font-size:40px;line-height:64px}
.event{position:absolute;top:58px;width:213px;height:252px;border:2px solid var(--purple);background:var(--purple)}
.event-photo{height:195px;background:linear-gradient(160deg,#c4a58f,#6a4a3a 60%,#3a2a2a)}
.event-label{height:55px;display:flex;align-items:center;justify-content:center;font-size:16px;font-weight:600}

/* news */
.news{top:1484px;height:516px;background:var(--purple)}
.section-title{position:absolute;left:0;width:1200px;text-align:center;font-size:42px}
.news .section-title{top:86px}
.news-card{position:absolute;width:473px;height:94px;border:2px solid var(--line);display:flex}
.news-date{width:84px;background:var(--white);color:var(--purple);font-weight:700;font-size:25px;line-height:30px;display:flex;flex-direction:column;align-items:center;justify-content:center}
.news-body{flex:1;padding:12px 16px 0 20px}
.news-body h3{font-size:15.5px;font-weight:600;margin-bottom:6px}
.news-body p{font-size:11.5px;line-height:21px;color:var(--muted)}
.news-icon{width:54px;border-left:2px solid var(--line);display:flex;align-items:center;justify-content:center}

/* books */
.books{top:2000px;height:323px}
.books-photo{position:absolute;inset:0;background:linear-gradient(90deg,#3a2418 0%,#6b4228 7%,#d9d6cf 30%,#f0eee9 60%,#cfcac0 85%,#4a2e20 100%)}
.books-panel{position:absolute;left:99px;top:0;width:256px;height:323px;background:rgba(62,35,114,.85)}
.books-title{position:absolute;left:126px;top:112px;font-size:40px;line-height:64px}
.book-feature{position:absolute;left:355px;top:0;width:746px;height:323px;background:rgba(62,35,114,.82)}
.book-cover{position:absolute;left:77px;top:49px;width:208px;height:221px;border:2px solid var(--white);background:radial-gradient(circle at 50% 60%,#c78a3a 0%,#5a3418 45%,#1c1410 100%)}
.book-cover .cover-title{position:absolute;top:26px;width:100%;text-align:center;font-weight:700;font-size:18px}
.book-cover .cover-author{position:absolute;right:12px;bottom:12px;font-size:13px}
.book-name{position:absolute;left:326px;top:75px;font-size:24px;font-weight:700}
.book-by{position:absolute;left:326px;top:122px;font-size:16px;font-weight:600}
.book-blurb{position:absolute;left:326px;top:156px;width:400px;font-size:11.8px;line-height:23px;color:var(--muted)}
.book-feature .dots{left:473px;top:265px}
.book-feature .dots span{width:11px;height:11px;border-width:1.5px}

/* biography */
.bio{top:2323px;height:430px;background:var(--purple)}
.bio .section-title{top:82px}
.bio-text{position:absolute;left:220px;top:172px;width:760px;text-align:center;font-size:11.8px;line-height:25px;color:var(--muted)}
.bio .btn{left:525px;top:292px;width:150px;height:46px;font-size:16px;font-weight:700}

/* footer */
.site-footer{top:2750px;height:211px;background:var(--night)}
.site-footer .curve{top:-2px;height:40px}
.footer-nav{position:absolute;left:99px;top:88px;display:flex;gap:46px;font-size:13px}
.footer-nav a{color:var(--white);text-decoration:none}
.copyright{position:absolute;left:99px;top:136px;font-size:12.5px;color:var(--muted)}
.social{position:absolute;left:868px;top:97px;display:flex;gap:13px}
.social span{width:48px;height:48px;border:2px solid var(--white);border-radius:50%}
</style>
</head>
<body>

<header class="site-header">
  <div class="brand script">Tessa Finch</div>
  <nav class="main-nav">
    <a href="#">HOME</a><a href="#">MY STORIES</a><a href="#">BOOKS</a><a href="#">NEWS</a><a href="#">CONTACT US</a>
  </nav>
</header>

<section class="hero">
  <div class="hero-photo" role="img" aria-label="Photo of a red-haired woman reading a book beside a lake under a tree"></div>
  <h1 class="hero-title script">Tessa Finch</h1>
  <p class="hero-tagline">I write serious stories, and I want that to come through.</p>
  <a class="btn" href="#">READ MORE</a>
  <svg class="curve" viewBox="0 0 1200 40" preserveAspectRatio="none" aria-hidden="true">
    <path d="M0 40 L0 30 C200 30 250 28 310 16 Q330 10 360 10 L840 10 Q870 10 890 16 C950 28 1000 30 1200 30 L1200 40 Z" fill="#3e2372"/>
    <path d="M0 30 C200 30 250 28 310 16 Q330 10 360 10 L840 10 Q870 10 890 16 C950 28 1000 30 1200 30" fill="none" stroke="#ffffff" stroke-width="2"/>
  </svg>
  <div class="dots"><span class="on"></span><span></span><span></span></div>
</section>

<section class="about">
  <div class="about-portrait" role="img" aria-label="Portrait photo of the author"></div>
  <h2 class="about-title script">About Me</h2>
  <p class="about-greet">Hi, I am Tessa Finch</p>
  <p class="about-text">I'm a new writer of literary fiction. Several of my short stories have been published in literary journals, with more to come. I'm working on my first novel, and one of my stories will be featured in a "best of" anthology that will hit bookstores soon. I write serious stories, and I want that to come through.</p>
  <a class="btn" href="#">READ MORE &gt;&gt;</a>
</section>

<section class="speaking">
  <div class="speaking-photo" role="img" aria-label="Photo of an open book on a wooden desk"></div>
  <div class="speaking-panel"></div>
  <h2 class="speaking-title script">Upcoming<br>Speaking<br>Engagements</h2>
  <article class="event" style="left:413px">
    <div class="event-photo" role="img" aria-label="Photo of a woman speaking into a microphone"></div>
    <div class="event-label">Speaking Engagement 1</div>
  </article>
  <article class="event" style="left:651px">
    <div class="event-photo" role="img" aria-label="Photo of a microphone in an empty hall"></div>
    <div class="event-label">Speaking Engagement 2</div>
  </article>
  <article class="event" style="left:888px">
    <div class="event-photo" role="img" aria-label="Photo of a woman presenting with a microphone"></div>
    <div class="event-label">Speaking Engagement 3</div>
  </article>
</section>

<section class="news">
  <h2 class="section-title script">Latest News</h2>
  <article class="news-card" style="left:99px;top:188px">
    <div class="news-date"><span>28</span><span>Aug</span></div>
    <div class="news-body"><h3>Lorem Ipsum is simply dummy</h3><p>All the Lorem Ipsum generators on the Internet tend repeat predefined chunks as necessary</p></div>
    <div class="news-icon"><svg width="34" height="30" viewBox="0 0 34 30" aria-hidden="true"><path d="M4 4h22a3 3 0 0 1 3 3v11a3 3 0 0 1-3 3H14l-7 6v-6H4a3 3 0 0 1-3-3V7a3 3 0 0 1 3-3z" fill="none" stroke="#fff" stroke-width="2.5"/><circle cx="15" cy="12.5" r="5.5" fill="#fff"/></svg></div>
  </article>
  <article class="news-card" style="left:626px;top:188px">
    <div class="news-date"><span>18</span><span>Aug</span></div>
    <div class="news-body"><h3>Lorem Ipsum is simply dummy</h3><p>All the Lorem Ipsum generators on the Internet tend repeat predefined chunks as necessary</p></div>
    <div class="news-icon"><svg width="34" height="30" viewBox="0 0 34 30" aria-hidden="true"><path d="M4 4h22a3 3 0 0 1 3 3v11a3 3 0 0 1-3 3H14l-7 6v-6H4a3 3 0 0 1-3-3V7a3 3 0 0 1 3-3z" fill="none" stroke="#fff" stroke-width="2.5"/><circle cx="15" cy="12.5" r="5.5" fill="#fff"/></svg></div>
  </article>
  <article class="news-card" style="left:99px;top:328px">
    <div class="news-date"><span>08</span><span>Aug</span></div>
    <div class="news-body"><h3>Lorem Ipsum is simply dummy</h3><p>All the Lorem Ipsum generators on the Internet tend repeat predefined chunks as necessary</p></div>
    <div class="news-icon"><svg width="34" height="30" viewBox="0 0 34 30" aria-hidden="true"><path d="M4 4h22a3 3 0 0 1 3 3v11a3 3 0 0 1-3 3H14l-7 6v-6H4a3 3 0 0 1-3-3V7a3 3 0 0 1 3-3z" fill="none" stroke="#fff" stroke-width="2.5"/><circle cx="15" cy="12.5" r="5.5" fill="#fff"/></svg></div>
  </article>
  <article class="news-card" style="left:626px;top:328px">
    <div class="news-date"><span>01</span><span>Aug</span></div>
    <div class="news-body"><h3>Lorem Ipsum is simply dummy</h3><p>All the Lorem Ipsum generators on the Internet tend repeat predefined chunks as necessary</p></div>
    <div class="news-icon"><svg width="34" height="30" viewBox="0 0 34 30" aria-hidden="true"><path d="M4 4h22a3 3 0 0 1 3 3v11a3 3 0 0 1-3 3H14l-7 6v-6H4a3 3 0 0 1-3-3V7a3 3 0 0 1 3-3z" fill="none" stroke="#fff" stroke-width="2.5"/><circle cx="15" cy="12.5" r="5.5" fill="#fff"/></svg></div>
  </article>
</section>

<section class="books">
  <div class="books-photo" role="img" aria-label="Photo of an open lined notebook with a pen on a wooden desk"></div>
  <div class="books-panel"></div>
  <h2 class="books-title script">My Book<br>Publications</h2>
  <div class="book-feature">
    <div class="book-cover" role="img" aria-label="Book cover of The Quiet Hours showing a glowing open book">
      <span class="cover-title">THE QUIET HOURS</span>
      <span class="cover-author">Tessa Finch</span>
    </div>
    <h3 class="book-name">The Quiet Hours</h3>
    <p class="book-by">By Tessa Finch</p>
    <p class="book-blurb">Ricardo says you cannot hear them. They slink like cats, he says. Ricardo says you cannot see them, not like you'd see your sister waiting on the curb for the school bus. They're in the shadows, he says. That flick in the corner of your eye? That's them, he says.</p>
    <div class="dots"><span></span><span></span><span class="on"></span></div>
  </div>
</section>

<section class="bio">
  <h2 class="section-title script">Biography</h2>
  <p class="bio-text">There are many variations of passages of Lorem Ipsum available, but the majority have suffered alteration in some form, by injected humour, or randomised words which don't look even slightly believable. If you are going to use a passage of Lorem Ipsum, you need to be sure there isn't anything embarrassing hidden in the middle of text. All the Lorem Ipsum generators on the Internet</p>
  <a class="btn" href="#">MY STORIES</a>
</section>

<footer class="site-footer">
  <svg class="curve" viewBox="0 0 1200 40" preserveAspectRatio="none" aria-hidden="true">
    <path d="M0 0 L0 10 C200 10 250 12 310 24 Q330 30 360 30 L840 30 Q870 30 890 24 C950 12 1000 10 1200 10 L1200 0 Z" fill="#3e2372"/>
    <path d="M0 10 C200 10 250 12 310 24 Q330 30 360 30 L840 30 Q870 30 890 24 C950 12 1000 10 1200 10" fill="none" stroke="#ffffff" stroke-width="2"/>
  </svg>
  <svg style="position:absolute;left:588px;top:8px" width="24" height="26" viewBox="0 0 24 26" aria-hidden="true"><path d="M3 13 L12 5 L21 13 M3 22 L12 14 L21 22" fill="none" stroke="#fff" stroke-width="2.5"/></svg>
  <nav class="footer-nav"><a href="#">Home</a><a href="#">My Stories</a><a href="#">Books</a><a href="#">News</a><a href="#">Contact Us</a></nav>
  <p class="copyright">© Copyright 2017 Tessa Finch. All Rights Reserved</p>
  <div class="social" aria-label="Social links"><span></span><span></span><span></span><span></span></div>
</footer>

</body>
</html>
```